Yard Sign Design for luxury design & build company

Looking to have 18" x 24" company yard signs designed.
An update to the business logo might be helpful.
Photos are not necessary but use if you can make inspiring.

Industry: Construction

Looking for a large headline of "Basement Finishing"
Website: www.tamberlyhomes.com
Phone Number (612) 555-0174
FB link: facebook.com/tamberlyhomesmn
Instagram: www.instagram.com/tamberlyhomesmn

Industry/Entity Type

Construction

Colors

Designer to choose colors to be used in the design.

Requirements
Must have
• Impactful high end characteristics
Nice to have
• Depth and detail graphis

```html
<!DOCTYPE html>
<html lang="en">
<head>
<meta charset="utf-8">
<title>Basement Finishing Yard Sign</title>
<link rel="stylesheet" href="https://fonts.googleapis.com/css2?family=Montserrat:wght@800;900&family=Roboto+Condensed:ital,wght@1,700&family=Cabin:wght@600&display=swap">
<style>
  :root {
    --page-bg: #ececec;
    --sign-red: #d7261f;
    --photo-red-dark: #a9312b;
    --photo-red-light: #d4584e;
    --ink: #0b0b0b;
    --paper: #ffffff;
  }
  html, body {
    margin: 0;
    width: 1200px;
    height: 807px;
    overflow: hidden;
    background: var(--page-bg);
  }
  .yard-sign {
    position: absolute;
    left: 80px;
    top: 13px;
    width: 1040px;
    height: 780px;
    display: block;
  }
  .sign-base { fill: var(--sign-red); }
  .website {
    font-family: "Roboto Condensed", "Arial Narrow", sans-serif;
    font-style: italic;
    font-weight: 700;
    font-size: 31px;
    fill: var(--paper);
  }
  .headline {
    font-family: "Montserrat", Arial, sans-serif;
    font-weight: 900;
    fill: var(--paper);
    stroke: var(--ink);
    stroke-linejoin: round;
    paint-order: stroke fill;
  }
  .headline-top { font-size: 180px; stroke-width: 14px; }
  .headline-bottom { font-size: 128px; stroke-width: 12px; }
  .phone {
    font-family: "Montserrat", Arial, sans-serif;
    font-weight: 800;
    font-size: 140px;
    fill: var(--paper);
    stroke: var(--ink);
    stroke-width: 9px;
    stroke-linejoin: round;
    paint-order: stroke fill;
  }
  .logo-panel { fill: var(--paper); }
  .logo-ring { fill: none; stroke: var(--sign-red); stroke-width: 4px; }
  .logo-name {
    font-family: "Montserrat", Arial, sans-serif;
    font-weight: 800;
    fill: var(--ink);
  }
  .social-frame { fill: none; stroke: var(--paper); stroke-width: 4px; }
  .social-link {
    font-family: "Cabin", "Gill Sans", sans-serif;
    font-weight: 600;
    font-size: 40px;
    fill: var(--paper);
    text-transform: uppercase;
  }
</style>
</head>
<body>
<svg class="yard-sign" viewBox="0 0 1040 780" xmlns="http://www.w3.org/2000/svg">
  <defs>
    <linearGradient id="room-tint" x1="0" y1="0" x2="1" y2="1">
      <stop offset="0" stop-color="var(--photo-red-light)"/>
      <stop offset="0.55" stop-color="#c2443b"/>
      <stop offset="1" stop-color="var(--photo-red-dark)"/>
    </linearGradient>
  </defs>

  <rect class="sign-base" x="0" y="0" width="1040" height="780"/>

  <rect class="room-photo" x="0" y="0" width="1040" height="588" fill="url(#room-tint)"
        role="img" aria-label="Finished basement living room with sectional sofa, fireplace and recessed lighting, tinted red"/>

  <text class="website" x="520" y="47" text-anchor="middle">www.tamberlyhomes.com</text>

  <text class="headline headline-top" x="57" y="235" textLength="922" lengthAdjust="spacingAndGlyphs">BASEMENT</text>
  <text class="headline headline-bottom" x="57" y="345" textLength="922" lengthAdjust="spacingAndGlyphs">FINISHING</text>

  <text class="phone" x="60" y="520" textLength="915" lengthAdjust="spacingAndGlyphs">(612) 555-0174</text>

  <rect class="logo-panel" x="11" y="600" width="170" height="168"/>
  <circle class="logo-ring" cx="96" cy="654" r="36"/>
  <text class="logo-name" x="96" y="727" text-anchor="middle" font-size="23" textLength="150" lengthAdjust="spacingAndGlyphs">TAMBERLY</text>
  <text class="logo-name" x="96" y="756" text-anchor="middle" font-size="15" letter-spacing="7">HOMES</text>

  <rect class="social-frame" x="183" y="602" width="845" height="164"/>
  <text class="social-link" x="201" y="668" textLength="808" lengthAdjust="spacingAndGlyphs">www.photoloop.com/tamberlyhomesmn</text>
  <text class="social-link" x="201" y="732" textLength="808" lengthAdjust="spacingAndGlyphs">www.friendhub.com/tamberlyhomesmn</text>
</svg>
</body>
</html>
```